Redesign two existing website pages and one new landing page for dental office

I need to redesign two webpages on my dental website, the Home page (http://brelvoortdental.com) and the Dental Implant Services page (http://www.brelvoortdental.com/dental-implant-services) and also create a landing page for the Dental Implant Services page.

Please use the same color scheme, slogans and subtitles for the redesign pages and create a reserved video spot on each page. The video spots should not be too big but not too small either and positioned in a central key location on each of the pages. The final redesigned pages should communicate leadership, confidence and trust.

The new landing page for the Dental implant Services page must not have any hyperlinks on the page and must entice the viewer to give name and email before downloading a "Free" eBook called "Is a Fresh Smile Worth Waiting For?" Any added photo images to this new page must be smiling.
Updates

Project Deadline Extended Reason: I got feedback that my project was not long enough so I'm extending it by 5 days. Added Thursday, April 16, 2015

Target Market(s)

People who are middle-age to seniors.

Industry/Entity Type

Dental

Coding

Coded - Design and coding required

Number of Pages Required

3 page

Requirements
Must have
• Compatible with existing website colors and theme.

```html
<!DOCTYPE html>
<html lang="en">
<head>
<meta charset="utf-8">
<title>Brelvoort Dental Care – Dental Implants</title>
<link href="https://fonts.googleapis.com/css2?family=Open+Sans:wdth,wght@75..100,400..800&display=swap" rel="stylesheet">
<style>
:root{
  --red:#e3201c;
  --red-dark:#a8120f;
  --ink:#2b2b2b;
  --body:#4a4a4a;
  --muted:#8a8a8a;
  --bar:#e4e4e4;
  --page:#ffffff;
  --footer:#f1f1f1;
  --video:#2f3338;
}
*{box-sizing:border-box;margin:0;padding:0}
html,body{width:1200px;height:2720px;overflow:hidden;background:var(--page)}
body{font-family:"Open Sans",Arial,sans-serif;color:var(--body);font-size:13.5px;line-height:1.55;position:relative}
.site-header{height:92px;display:flex;align-items:center;justify-content:space-between;padding:0 180px}
.brand{display:flex;align-items:center;gap:12px;font-size:30px;font-weight:600;color:#6d7b86;letter-spacing:-.5px}
.brand-dot{width:22px;height:22px;border-radius:50%;background:#6d7b86}
.call{font-size:17px;color:var(--muted)}
.call strong{color:var(--ink);font-weight:700}
.hero{position:relative;height:468px;background:linear-gradient(90deg,#5d6b3a 0%,#a4b36c 22%,#c9b196 45%,#9fae6a 70%,#6f7f3f 100%)}
.hero-photo{position:absolute;inset:0}
.lead-form{position:absolute;left:735px;top:8px;width:345px;height:470px;background:var(--red);padding:26px 28px 0;box-shadow:0 4px 14px rgba(0,0,0,.35)}
.lead-form::after{content:"";position:absolute;right:0;bottom:0;border-style:solid;border-width:0 0 40px 40px;border-color:transparent transparent var(--red-dark) transparent}
.lead-form h2{color:#fff;font-weight:800;font-stretch:75%;font-size:32px;line-height:1.12;text-align:center;margin-bottom:8px}
.ebook-note{color:#fff;font-size:12.5px;line-height:1.35;text-align:center;margin-bottom:16px}
.ebook-note strong{font-weight:700}
.field{display:flex;align-items:center;height:36px;margin-bottom:8px}
.field label{width:100px;color:#fff;font-size:13px;text-align:center}
.field span{flex:1;height:30px;background:#fff;border:1px solid #bbb}
.lead-form .submit{display:block;margin:16px auto 0;width:290px;height:66px;border-radius:10px;background:linear-gradient(#ffffff,#d6d6d6);border:1px solid #999;color:var(--red);font-weight:700;font-size:30px;line-height:64px;text-align:center}
.content{width:840px;margin:0 auto;padding-top:36px}
.intro h1{font-size:23px;line-height:1.3;color:var(--ink);font-weight:700;margin-bottom:14px}
p{margin-bottom:12px}
.with-art{display:flex;gap:26px;align-items:flex-start}
.with-art .text{flex:1}
.art{flex:none;border-radius:4px}
.art-implant{width:240px;height:150px;background:linear-gradient(135deg,#f2d6d6,#eab7b7 45%,#d8d8d8 70%,#f4f4f4)}
.art-bridge{width:250px;height:170px;background:linear-gradient(135deg,#f1cfcf,#e4a9a9 50%,#ececec)}
.art-arch{width:290px;height:230px;background:radial-gradient(ellipse at 50% 40%,#f6dada,#e38b8b 55%,#f3f3f3 80%)}
.art-denture{width:300px;height:250px;background:radial-gradient(ellipse at 50% 50%,#f4f4f4,#e4a4a4 55%,#f7f7f7 80%)}
.video-spot{flex:none;width:340px;height:192px;background:var(--video);border-radius:4px;display:flex;align-items:center;justify-content:center}
.section{margin-top:22px}
.bar{background:var(--bar);font-size:19px;font-weight:700;color:var(--ink);padding:8px 14px;margin-bottom:14px}
.site-footer{position:absolute;left:0;right:0;bottom:0;height:72px;background:var(--footer);border-top:1px solid #ddd;text-align:center;line-height:72px;font-size:12px;color:var(--muted)}
</style>
</head>
<body>
<header class="site-header">
  <div class="brand"><span class="brand-dot"></span>Brelvoort Dental Care</div>
  <div class="call">Call Us Today <strong>(281) 555-0147</strong></div>
</header>

<section class="hero">
  <div class="hero-photo" role="img" aria-label="Smiling woman with long dark hair outdoors against a soft green background"></div>
  <form class="lead-form">
    <h2>GET MORE INFO<br>ABOUT DENTAL IMPLANTS</h2>
    <p class="ebook-note">Plus our <strong>FREE eBook</strong>: “Is a Fresh Smile Worth Waiting For?”</p>
    <div class="field"><label>First Name</label><span></span></div>
    <div class="field"><label>Last Name</label><span></span></div>
    <div class="field"><label>Phone</label><span></span></div>
    <div class="field"><label>Email</label><span></span></div>
    <div class="submit">GET MORE INFO!</div>
  </form>
</section>

<main class="content">
  <section class="intro">
    <h1>Dr. Paul Brelvoort: The Sugar Land Cosmetic Dentist Giving Attractive Smile Makeovers with Dental Implants</h1>
    <div class="with-art">
      <div class="text">
        <p>Sugarland TX dental implants center are you suffering from severe tooth decay? Are your teeth badly damaged? Do you have missing teeth? These are some of the reasons why people do not flash their pearly whites in public. If you can identify with such people, it is time to enjoy the affordable and exceptional dental implant services of Dr. Paul Brelvoort, DDS FAGD.</p>
        <p>Brelvoort Dental Care has been successfully serving Sugar Land TX for several years, restoring smiles at our dental implant center. Dr. Brelvoort has been dedicated to providing attractive new smiles to his patients using the latest techniques in dental implants. If you are looking to regain a natural smile that showcases bright white teeth, look no further than dental implants with Dr. Brelvoort.</p>
      </div>
      <div class="art art-implant" role="img" aria-label="Illustration of a dental implant post and crown beside natural teeth"></div>
    </div>
  </section>

  <section class="section">
    <h2 class="bar">Understanding Dental Implants</h2>
    <p>Dental implants have truly revolutionized smile reconstruction. Missing teeth, severely damaged teeth and extreme tooth decay can easily be treated with the help of these implants and restore peoples self-confidence and self-esteem.</p>
    <p>When the dental implant procedure is performed accurately and correctly, the results can be astonishing. No one will know you have implants, even when you flash a smile.</p>
    <p>A dental implant consists of a small titanium post or screw that is surgically implanted into your jawbone. After dental implant placement, and a few months recuperation period, the surface of the implant fuses with your jawbone. The result is a sturdy and strong base which can be used as an anchor for attaching a dental prosthesis such as a crown, a fixed bridge or a denture.</p>
    <p>Dr. Brelvoort has helped hundreds of clients regain their self-confidence and beautiful smiles with the help of dental implants. So, if you are looking for an experienced and skilled dental implant dentist in Sugar Land TX, your search ends with Dr. Paul Brelvoort.</p>
  </section>

  <section class="section">
    <h2 class="bar">See How Dental Implants Work</h2>
    <div class="with-art">
      <div class="text">
        <p>Watch Dr. Brelvoort walk through each step of the implant process, from the first consultation and 3D scan to the day your new teeth are placed.</p>
        <p>Many of our patients are surprised by how comfortable the treatment is. Gentle sedation, careful planning and a calm team help you feel at ease throughout every visit.</p>
        <p>Once healed, implants feel and work like natural teeth. You can enjoy your favorite foods, speak with confidence and smile freely again for many years to come.</p>
      </div>
      <div class="video-spot" role="img" aria-label="Video player: dental implant procedure overview">
        <svg width="64" height="64" viewBox="0 0 64 64" aria-hidden="true"><circle cx="32" cy="32" r="30" fill="none" stroke="#fff" stroke-width="3"/><path d="M26 20 L46 32 L26 44 Z" fill="#fff"/></svg>
      </div>
    </div>
  </section>

  <section class="section">
    <h2 class="bar">Single Tooth Dental implants Restored with a Crown</h2>
    <p>Accidents and periodontal diseases cause people to lose a single tooth. If you have lost a single tooth, it is possible to replace it using a dental implant. A dental implant makes sure that the original structure of the tooth is retained without any gaps. The dentist places the dental implant in the gap created by the missing tooth. After the implant is placed in the jawbone, a small post known as abutment is fixed onto it. The porcelain crown, which looks and works like a natural tooth, is then fixed on the abutment using dental cement.</p>
  </section>

  <section class="section">
    <h2 class="bar">Multiple Tooth Dental Implants Restored with a Bridge</h2>
    <div class="with-art">
      <div class="text">
        <p>For various reasons, people start losing multiple teeth after a certain age. Multiple dental implants are one of the best options for such people. Multiple tooth loss is common among aging people or those who have sustained a trauma on the mouth. Even with good dental hygiene, it is possible to lose teeth gradually. Having too many missing teeth is detrimental to your confidence at any age. Several missing teeth can result in speech impairment and digestive problems, as the person will be unable to chew food properly. Dental implants offer an ideal solution for such a problem, as they improve the appearance of the person and this results in better self-confidence and self-image.</p>
      </div>
      <div class="art art-bridge" role="img" aria-label="Illustration of an implant-supported bridge replacing several teeth"></div>
    </div>
    <p>After examining the structure and the condition of the jawbone, it may be necessary for a dentist to perform AO4 or All-on-Four treatment. Bone deterioration typically takes place under the gums and is barely noticeable. If there is such a condition then this treatment is essential, as the bone will not be able to support dental implants.</p>
  </section>

  <section class="section">
    <h2 class="bar">All-On-Four (AO4) Dental Implants Restored with a Screw Retained Denture</h2>
    <div class="with-art">
      <div class="text">
        <p>The AO4 is a permanent solution to replace all the teeth in the mouth. It makes use of a denture-like arched structure for both the upper and lower jaw. This treatment is done using 4 posts for each jaw (upper and lower). You may wonder why should there are 4 posts. Many dentists find this as an optimal number to provide a permanent solution for missing teeth. A bridge can be sturdily placed on to the jawbone using these four posts. The four points provide the support columns for the teeth structure and they also help to take the load of the denture.</p>
      </div>
      <div class="art art-arch" role="img" aria-label="Illustration of a full arch denture seated on four implant posts"></div>
    </div>
    <div class="with-art" style="margin-top:14px">
      <div class="art art-denture" role="img" aria-label="Illustration of a screw retained denture above an implanted lower jaw"></div>
      <div class="text">
        <p>All-on-four dental implants are very similar to the concept of roadway bridges. Just like a bridge is supported using columns at frequent intervals, even the dental bridges use four posts to support each bridge. These dental implants can give you a smile makeover and restore the lost function of your teeth. You will be able to chew, speak clearly, bite and smile without feeling self-conscious.</p>
        <p>Different types of dental implants can give you a lasting set of teeth and keep you smiling for the rest of your life. Do not let lost teeth reduce the quality of your life or lower your self-esteem. Instead opt for dental implants and transform your face and life for the better.</p>
      </div>
    </div>
  </section>
</main>

<footer class="site-footer">©2015 Brelvoort Dental Care, Crestview Medical Plaza, 2400 Meadow Crest Blvd, Ste. 210, Sugar Land, TX 77479</footer>
</body>
</html>
```